Lotus Bay Catering Group - Business Card Design

We are premium Asian Catering Company based in Melbourne. We specialize in full service sit down banquets.

Industry/Entity Type

Business

Contact Information for Business Card

Lotus Bay Catering Group
17b Harwick Ave Kelvindale 3194
P: 03 9417 2658 | M: 0438 672 915
www.lotusbaycatering.com.au
info@lotusbaycatering.com.au

```html
<!DOCTYPE html>
<html lang="en">
<head>
<meta charset="utf-8">
<title>Lotus Bay Catering Group – Business Card</title>
<link href="https://fonts.googleapis.com/css2?family=Cinzel:wght@400;700&family=Marcellus&display=swap" rel="stylesheet">
<style>
  :root {
    --page: #ffffff;
    --card-dark: #050505;
    --card-dark-mid: #1c1c1c;
    --frame: #ffffff;
    --brand-red: #c0252b;
    --ink: #333333;
    --ink-soft: #5a5a5a;
    --icon-grey: #9a9a9a;
    --card-border: #8a8a8a;
    --hex-light: #f1f1f1;
  }
  * { margin: 0; padding: 0; box-sizing: border-box; }
  html, body { width: 1200px; height: 900px; overflow: hidden; background: var(--page); }
  .canvas { position: relative; width: 1200px; height: 900px; }

  /* Front card */
  .card-front {
    position: absolute; left: 330px; top: 95px; width: 577px; height: 334px;
    background: var(--card-dark);
  }
  .card-front__texture {
    position: absolute; inset: 0;
    background: radial-gradient(ellipse at 50% 45%, var(--card-dark-mid) 0%, #0b0b0b 55%, var(--card-dark) 100%);
  }
  .card-front__frame {
    position: absolute; left: 13px; top: 12px; width: 551px; height: 307px;
    border: 3px solid var(--frame);
  }
  .card-front__mark {
    position: absolute; left: 258px; top: 104px; width: 62px; height: 62px;
    border-radius: 50%; background: var(--brand-red);
  }
  .card-front__brand {
    position: absolute; left: 0; right: 0; top: 176px; text-align: center;
    font-family: "Cinzel", serif; font-weight: 700; color: var(--frame);
    font-size: 24px; line-height: 1.2; letter-spacing: 0.5px;
  }

  /* Back card */
  .card-back {
    position: absolute; left: 330px; top: 454px; width: 574px; height: 326px;
    background: #fff; border: 1px solid var(--card-border); overflow: hidden;
  }
  .card-back__texture {
    position: absolute; inset: 0;
    background: linear-gradient(135deg, #fafafa 0%, var(--hex-light) 50%, #fafafa 100%);
  }
  .card-back__mini-brand {
    position: absolute; left: 9px; top: 10px; width: 48px; text-align: center;
    font-family: "Cinzel", serif; font-weight: 700; color: var(--brand-red);
    font-size: 7px; line-height: 1.1;
  }
  .card-back__mini-mark {
    display: block; width: 14px; height: 14px; border-radius: 50%;
    background: var(--brand-red); margin: 0 auto 3px;
  }
  .card-back__title {
    position: absolute; left: 163px; top: 13px;
    font-family: "Cinzel", serif; font-weight: 400; font-size: 20px; color: var(--brand-red); letter-spacing: 0.3px;
  }
  .card-back__tagline {
    position: absolute; left: 218px; top: 38px;
    font-family: "Cinzel", serif; font-size: 8.5px; color: var(--ink);
  }
  .card-back__divider {
    position: absolute; left: 304px; top: 51px; width: 2px; height: 227px;
    background: var(--brand-red);
  }
  .card-back__logo {
    position: absolute; left: 50px; top: 98px; width: 220px; text-align: center;
    font-family: "Cinzel", serif; font-weight: 700; color: var(--brand-red);
    font-size: 22px; line-height: 1.25;
  }
  .card-back__logo-mark {
    display: block; width: 80px; height: 80px; border-radius: 50%;
    background: var(--brand-red); margin: 0 auto 14px;
  }
  .card-back__corner { position: absolute; left: 14px; top: 252px; }

  .contact-list { position: absolute; left: 320px; top: 110px; list-style: none; }
  .contact-item { position: absolute; left: 0; display: flex; align-items: center; white-space: nowrap; }
  .contact-item svg { width: 20px; height: 20px; flex: none; }
  .contact-item__text { margin-left: 23px; color: var(--ink); }
  .contact-item--phone .contact-item__text { font-family: "Marcellus", serif; font-size: 26px; }
  .contact-item--small .contact-item__text { font-family: "Cinzel", serif; font-size: 11px; line-height: 1.6; }

  .card-back__web {
    position: absolute; left: 204px; top: 295px;
    font-family: Arial, Helvetica, sans-serif; font-size: 15px; color: var(--ink-soft);
  }
</style>
</head>
<body>
<main class="canvas">

  <section class="card-front" aria-label="Business card front">
    <div class="card-front__texture" role="img" aria-label="Dark hexagon mesh background pattern"></div>
    <div class="card-front__frame"></div>
    <span class="card-front__mark"></span>
    <div class="card-front__brand">LOTUS BAY<br>CATERING GROUP</div>
  </section>

  <section class="card-back" aria-label="Business card back">
    <div class="card-back__texture" role="img" aria-label="Faint light grey hexagon background pattern"></div>

    <div class="card-back__mini-brand"><span class="card-back__mini-mark"></span>LOTUS BAY</div>

    <h1 class="card-back__title">Lotus Bay Catering Group</h1>
    <p class="card-back__tagline">Premium Asian Catering Company</p>

    <div class="card-back__logo"><span class="card-back__logo-mark"></span>LOTUS BAY<br>CATERING GROUP</div>

    <svg class="card-back__corner" width="50" height="56" viewBox="0 0 50 56" aria-hidden="true">
      <polygon points="0,0 0,56 50,56" fill="#2a2a2a"/>
    </svg>

    <div class="card-back__divider"></div>

    <ul class="contact-list">
      <li class="contact-item contact-item--phone" style="top:-2px">
        <svg viewBox="0 0 20 20" aria-hidden="true"><circle cx="10" cy="10" r="9" fill="none" stroke="var(--icon-grey)" stroke-width="1.5"/><path d="M7 5.5l1.6 2.3-1 1.1c.6 1.3 1.4 2.1 2.6 2.7l1.1-1 2.2 1.6-.8 1.6c-3.3.1-6.5-3.1-6.4-6.5z" fill="var(--icon-grey)"/></svg>
        <span class="contact-item__text">0438 672 915</span>
      </li>
      <li class="contact-item contact-item--phone" style="top:31px">
        <svg viewBox="0 0 20 20" aria-hidden="true"><circle cx="10" cy="10" r="9" fill="none" stroke="var(--icon-grey)" stroke-width="1.5"/><path d="M7 5.5l1.6 2.3-1 1.1c.6 1.3 1.4 2.1 2.6 2.7l1.1-1 2.2 1.6-.8 1.6c-3.3.1-6.5-3.1-6.4-6.5z" fill="var(--icon-grey)"/></svg>
        <span class="contact-item__text">03 9417 2658</span>
      </li>
      <li class="contact-item contact-item--small" style="top:76px">
        <svg viewBox="0 0 20 20" aria-hidden="true"><circle cx="10" cy="10" r="9.5" fill="var(--icon-grey)"/><rect x="5" y="6.5" width="10" height="7" fill="#fff"/><path d="M5 6.5l5 4 5-4" fill="none" stroke="var(--icon-grey)" stroke-width="1"/></svg>
        <span class="contact-item__text">info@lotusbaycatering.com.au</span>
      </li>
      <li class="contact-item contact-item--small" style="top:109px; align-items:flex-start">
        <svg viewBox="0 0 20 20" aria-hidden="true"><circle cx="10" cy="10" r="9.5" fill="var(--icon-grey)"/><path d="M4.5 10.5L10 5.5l5.5 5h-1.5v4h-2.5v-3h-3v3H6v-4z" fill="#fff"/></svg>
        <span class="contact-item__text">17b Harwick Ave<br>Kelvindale 3194</span>
      </li>
    </ul>

    <p class="card-back__web">www.lotusbaycatering.com.au</p>
  </section>

</main>
</body>
</html>
```